DOG DAYCARE BILLBOARD

Design a bold exciting billboard that can be read easily from a distance! Our goal is brand awareness and showcasing the services we offer (Boarding, Grooming, Daycare, and Training.
we would like to see examples with the phrase "your best friend's best day". Our name Bright Meadow Canine Activity Center (or just Bright Meadow might work better and could be bigger) and the services we provide.
(there are two examples of what we like included in the pictures)
you can find more information o our website at pawplayhub@mailnest.example.

```html
<!DOCTYPE html>
<html lang="en">
<head>
<meta charset="utf-8">
<title>Bright Meadow Billboard</title>
<link rel="stylesheet" href="https://fonts.googleapis.com/css2?family=Poppins:wght@600;700&family=Allura&display=swap">
<style>
  :root {
    --lime: #a6ce39;
    --ink: #0d0d0d;
    --paper: #ffffff;
    --backdrop: #1c1f26;
    --photo-dark: #2b2b2e;
    --photo-mid: #4a4a50;
  }
  * { margin: 0; padding: 0; box-sizing: border-box; }
  html, body { width: 1200px; height: 900px; overflow: hidden; }
  body { background: var(--backdrop); position: relative; font-family: "Poppins", sans-serif; }

  .billboard {
    position: absolute; left: 50px; top: 153px;
    width: 1100px; height: 594px;
    background: var(--lime);
    padding: 10px;
  }
  .billboard__face {
    position: relative; width: 100%; height: 100%;
    background: var(--paper); overflow: hidden;
  }

  .brand {
    position: absolute; left: 232px; top: 58px;
    display: flex; align-items: center; gap: 14px;
  }
  .brand__dot { width: 28px; height: 28px; border-radius: 50%; background: var(--ink); }
  .brand__name {
    font-weight: 700; font-size: 36px; color: var(--ink);
    letter-spacing: 0.5px; line-height: 1;
  }
  .brand__tagline {
    position: absolute; left: 274px; top: 106px;
    font-weight: 600; font-size: 14px; letter-spacing: 2px;
    text-transform: uppercase; color: var(--ink);
  }

  .headline { position: absolute; inset: 0; font-weight: 700; }
  .headline__bold {
    position: absolute; font-weight: 700; font-size: 58px;
    color: var(--ink); line-height: 1; white-space: nowrap;
  }
  .headline__your { left: 62px; top: 214px; }
  .headline__day { left: 420px; top: 318px; }
  .headline__script {
    position: absolute; left: 368px; top: 198px;
    font-family: "Allura", cursive; font-weight: 400; font-size: 104px;
    color: var(--lime); line-height: 1; white-space: nowrap;
  }

  .services-band {
    position: absolute; left: 0; right: 0; bottom: 0; height: 128px;
    background: var(--ink);
  }
  .location-tab {
    position: absolute; left: 148px; top: 408px;
    height: 54px; padding: 0 26px 0 20px;
    background: var(--lime);
    display: flex; align-items: center; gap: 12px;
    font-weight: 600; font-size: 21px; text-transform: uppercase;
    color: var(--ink); letter-spacing: 0.3px;
  }
  .location-tab svg { width: 18px; height: 26px; }

  .services {
    position: absolute; left: 36px; bottom: 30px;
    display: flex; align-items: center; list-style: none;
  }
  .services__item {
    font-weight: 600; font-size: 32px; color: var(--lime);
    padding: 0 16px; line-height: 1.2;
    border-left: 2px solid var(--paper);
  }
  .services__item:first-child { border-left: none; padding-left: 0; }

  .hero-photo {
    position: absolute; right: 24px; top: 64px;
    width: 262px; height: 510px;
    background: linear-gradient(160deg, var(--photo-mid), var(--photo-dark) 70%);
    border-radius: 120px 120px 0 0;
  }
</style>
</head>
<body>
  <div class="billboard">
    <div class="billboard__face">
      <div class="brand">
        <span class="brand__dot"></span>
        <span class="brand__name">Bright Meadow</span>
      </div>
      <div class="brand__tagline">Canine Activity Center</div>

      <h1 class="headline">
        <span class="headline__bold headline__your">Your Best</span>
        <span class="headline__script">Friend's</span>
        <span class="headline__bold headline__day">Best Day</span>
      </h1>

      <div class="services-band"></div>
      <div class="location-tab">
        <svg viewBox="0 0 18 26" aria-hidden="true">
          <path d="M9 0C4 0 0 4 0 9c0 6.5 9 17 9 17s9-10.5 9-17C18 4 14 0 9 0z" fill="#ffffff"/>
          <circle cx="9" cy="9" r="3.5" fill="#a6ce39"/>
        </svg>
        Visit us in Maple Ridge, IA
      </div>
      <ul class="services">
        <li class="services__item">Boarding</li>
        <li class="services__item">Grooming</li>
        <li class="services__item">Daycare</li>
        <li class="services__item">Training</li>
      </ul>

      <div class="hero-photo" role="img" aria-label="Photo of a black French bulldog wearing rainbow sunglasses and a rainbow bandana"></div>
    </div>
  </div>
</body>
</html>
```